Design the most beautiful 'value book' for our team

We have a book that describes the value of the team. Each value is illustrated through stories told by the team members (5 to 6 per value).
The purpose of the 'value book' is for every new team members to read it and be inspired by it. It's also a reference of existing team members.
The value book will be displayed in public areas in the company. Any employees from other teams can pick it up and read it, and hopefully embrace the values described in the book.

We would like the value book to have a professional, minimalist design with fresh colors. When people pick it up, we want them to feel curious and think 'what is this magazine?' and when they open it, we want them to go through each pages because they are so beautiful by design.

An excerpt of the book is enclosed (book preface + first value)

Font styles to use
Serif
Sans Serif

Requirements
Must have
• Attractive cover
• Consistent theme throughout the book
• Design allows to easily add more stories as time goes by
• Pagination
• Table of content
Should not have
• No stock photos / images (ok to use graphics and other visuals)

```html
<!DOCTYPE html>
<html lang="en">
<head>
<meta charset="utf-8">
<title>The Nova Value Book</title>
<link rel="stylesheet" href="https://fonts.googleapis.com/css2?family=Ubuntu:wght@400;500;700&family=Ubuntu+Condensed&family=Saira+Extra+Condensed:wght@200;300&family=Raleway:wght@300&display=swap">
<style>
:root{
  --bg:#ececec;
  --space-deep:#1c1524;
  --space-mid:#4a3a62;
  --space-glow:#b9a6cc;
  --title:#f1ecf4;
  --title-accent:#c9a8de;
  --paper-left:#e4ebe7;
  --paper-teal:#9fb3b6;
  --paper-right:#e8ede5;
  --ink:#2a2f33;
  --heading:#3a4a52;
  --lilac:#b7a6cc;
  --lilac-dark:#9d8ab8;
  --white:#ffffff;
  --photo-rose:#8a4a50;
  --photo-grey:#b9bfbd;
  --tree:#e3b6b2;
}
*{box-sizing:border-box;margin:0;padding:0}
html,body{width:798px;height:1200px;overflow:hidden;background:var(--bg)}
.canvas{position:relative;width:798px;height:1200px;background:linear-gradient(#f3f3f3,#e2e2e2)}
.spread{position:absolute;left:59px;width:680px;height:480px;box-shadow:0 6px 18px rgba(0,0,0,.18)}
.spread--cover{top:60px}
.spread--inside{top:650px}
.page{position:absolute;top:0;width:340px;height:480px;overflow:hidden}
.page--left{left:0}
.page--right{left:340px}

/* cover */
.galaxy{position:absolute;inset:0;background:
  radial-gradient(ellipse 220px 140px at 210px 190px,var(--space-glow),transparent 70%),
  radial-gradient(ellipse 360px 260px at 260px 220px,var(--space-mid),transparent 75%),
  var(--space-deep)}
.cover-visual{position:absolute;top:165px;left:45px;width:250px;height:250px;border-radius:50%;z-index:1;
  background:radial-gradient(circle at 50% 40%,#f6d9bf,#d9a88a 45%,#3a3340 75%,#141018)}
.cover-author{position:absolute;top:26px;left:0;width:340px;text-align:center;font:300 12px 'Raleway',sans-serif;letter-spacing:9px;color:var(--title);z-index:2}
.cover-title{position:absolute;top:50px;left:0;width:340px;text-align:center;font:300 38px/36px 'Saira Extra Condensed',sans-serif;color:var(--title);letter-spacing:1px;z-index:2}
.cover-title .accent{color:var(--title-accent)}

/* inside */
.page--left .paper{position:absolute;inset:0;background:linear-gradient(160deg,var(--paper-teal),var(--paper-left) 45%)}
.page--right .paper{position:absolute;inset:0;background:linear-gradient(200deg,var(--paper-teal),var(--paper-right) 45%)}
.heading{position:absolute;font:400 24px/24px 'Ubuntu Condensed',sans-serif;color:var(--heading)}
.heading .light{color:var(--white)}
.body{position:absolute;font:500 6.6px/8.2px 'Ubuntu',sans-serif;color:var(--ink);z-index:2}
.body p{margin-bottom:5px}
.pen-art{position:absolute;top:72px;left:210px;width:90px;height:36px;background:linear-gradient(90deg,transparent,#8a8f8f 60%,transparent)}
.photo-kid{position:absolute;left:170px;top:300px;width:170px;height:180px;background:linear-gradient(170deg,rgba(255,255,255,0),#c98b8f 35%,var(--photo-rose) 70%,#5e3a3e)}
.photo-kids{position:absolute;left:0;top:345px;width:120px;height:135px;background:linear-gradient(180deg,rgba(255,255,255,0),var(--photo-grey) 50%,#8c928f)}
.tree-art{position:absolute;top:80px;right:-10px;width:190px;height:210px;border-radius:40% 40% 10% 10%;background:radial-gradient(ellipse at 50% 45%,var(--tree),rgba(227,182,178,0) 70%)}
.folio{position:absolute;bottom:14px;height:16px;display:flex;align-items:center;z-index:3}
.folio-num{width:16px;height:16px;border-radius:50%;background:var(--white);font:700 6px/16px 'Ubuntu',sans-serif;text-align:center;color:var(--ink)}
.folio-line{height:1px;width:250px;background:var(--white)}
.page--left .folio{left:16px}
.page--left .folio-line{margin-left:6px}
.page--right .folio{right:16px}
.page--right .folio-line{margin-right:6px;width:170px}
.values-box{position:absolute;left:128px;top:318px;width:196px;height:132px;background:linear-gradient(135deg,var(--lilac),var(--lilac-dark))}
.value{position:absolute;width:80px;text-align:center;font:400 5.6px 'Ubuntu',sans-serif;color:var(--white);text-transform:uppercase;letter-spacing:.3px}
.value svg{display:block;margin:0 auto 2px;width:22px;height:22px;fill:none;stroke:var(--white);stroke-width:1.3;stroke-linecap:round;stroke-linejoin:round}
</style>
</head>
<body>
<div class="canvas">

  <section class="spread spread--cover">
    <div class="galaxy" role="img" aria-label="Purple galaxy of stars spanning back and front cover"></div>
    <div class="page page--right">
      <div class="cover-visual" role="img" aria-label="Glowing brain over a planet with a man's profile in silhouette"></div>
      <div class="cover-author">AUTHOR NAME</div>
      <h1 class="cover-title">THE<br>NOVA <span class="accent">VALUE</span><br>BOOK</h1>
    </div>
  </section>

  <section class="spread spread--inside">
    <div class="page page--left">
      <div class="paper"></div>
      <h2 class="heading" style="left:20px;top:22px">Why did we write<br>this book ?</h2>
      <div class="pen-art" role="img" aria-label="Sketch of a hand holding a pen"></div>
      <div class="photo-kids" role="img" aria-label="Faded photo of a group of children"></div>
      <div class="photo-kid" role="img" aria-label="Photo of a child in a knitted hat seen from behind"></div>
      <div class="body" style="left:20px;top:82px;width:140px">
        <p>Every company has a vision, a set of values and a unique culture. Every team should have its own vision, its own set of values and its own culture. Both things aren't necessarily exactly the same. However they must be in alignment.</p>
        <p>We believe that values are what makes the identity of a team. Identity gives you a sense of pride, safety and belonging. It also gives you a strong foundation from which to grow and become more.</p>
        <p>Without an identity, a team is just a group of people trying to lay bricks individually. With an identity, a team can build a cathedral.</p>
        <p>By reflecting on what is the most important in a team, you establish a sense of clarity. And only with clarity can you navigate in this chaotic working environment.</p>
        <p>In 'easy' time, our values carry us in places we didn't know we could go. When the difficult times arise, we rely on our values to make key decisions.</p>
        <p>Such decisions include how to behave and not behave. Who to hire and who to let go of. What to tolerate and to what extent. In which activities to engage in and be focused on. And which activities to let other teams handle.</p>
      </div>
      <div class="body" style="left:180px;top:118px;width:140px">
        <p>This book was written by the NOVA team members. It describes our identity, who we are.</p>
        <p>We hope this book will be a source of inspiration for you.</p>
        <p>In any case, we highly recommend you to reflect upon it.</p>
        <p>What's your true identity?</p>
        <p>Feel free to reach out to any of the NOVA team members for further discussion.</p>
      </div>
      <div class="folio"><span class="folio-num">01</span><span class="folio-line"></span></div>
    </div>

    <div class="page page--right">
      <div class="paper"></div>
      <div class="tree-art" role="img" aria-label="Faint pink bare tree"></div>
      <h2 class="heading" style="left:26px;top:40px">How is <span class="light">this book</span><br>organized?</h2>
      <div class="body" style="left:26px;top:100px;width:150px">
        <p>We could have compiled a shortlist of what we value the most and give it to you. But you wouldn't read it, because it'd be so boring and meaningless.</p>
        <p>Instead we took some time to reflect on our core values, and why. This lead us to share a variety of stories.</p>
        <p>You will find in this book a series of story from each team members. Each story illustrates a core value.</p>
      </div>
      <div class="body" style="left:128px;top:288px;width:196px">
        <p>To make it easier for you to navigate in this book, here are our 6 team values (in no particular order):</p>
      </div>
      <div class="values-box">
        <div class="value" style="left:10px;top:10px">
          <svg viewBox="0 0 24 24"><path d="M3 3v18h18"/><path d="M6 16l5-5 3 3 6-7"/><path d="M16 7h4v4"/></svg>Growth</div>
        <div class="value" style="left:106px;top:10px">
          <svg viewBox="0 0 24 24"><path d="M12 3l8 4v10l-8 4-8-4V7z"/><path d="M4 7l8 4 8-4M12 11v10"/></svg>Contribution</div>
        <div class="value" style="left:10px;top:52px">
          <svg viewBox="0 0 24 24"><path d="M6 3h9l4 4v14H6z"/><path d="M9 10h7M9 14h7M9 18h5"/></svg>Result oriented</div>
        <div class="value" style="left:106px;top:52px">
          <svg viewBox="0 0 24 24"><path d="M2 11l5-4 5 3 5-3 5 4"/><path d="M7 13l4 4 4-4"/></svg>Understanding</div>
        <div class="value" style="left:10px;top:94px">
          <svg viewBox="0 0 24 24"><circle cx="12" cy="12" r="4"/><circle cx="12" cy="3" r="1.5"/><circle cx="12" cy="21" r="1.5"/><circle cx="3" cy="12" r="1.5"/><circle cx="21" cy="12" r="1.5"/></svg>Innovation</div>
        <div class="value" style="left:106px;top:94px">
          <svg viewBox="0 0 24 24"><path d="M12 22V12M12 12L5 5M12 12l7-7M12 2v4"/><path d="M5 9V5h4M15 5h4v4M10 4l2-2 2 2"/></svg>Flexibility</div>
      </div>
      <div class="body" style="left:26px;top:408px;width:96px">
        <p>We wish you to enjoy this book. If it inspires you, spread the word!</p>
      </div>
      <div class="folio"><span class="folio-line"></span><span class="folio-num">02</span></div>
    </div>
  </section>

</div>
</body>
</html>
```